Tallow Crest Business Card

We need a business card designed for a a company called "Tallow Crest". We offer consulting, coaching and training to business leaders and coaches (across the world) using the latest findings in neuroscience, social and emotional intelligence and positive psychology. The final design should communicate the use of brain science to create sustainable relationships.

The card should be doublesided. The logo is attached and names and titles will be provided to the successful designer. Thank you.

Industry/Entity Type

Training

```html
<!DOCTYPE html>
<html lang="en">
<head>
<meta charset="utf-8">
<title>Tallow Crest Business Card</title>
<link rel="stylesheet" href="https://fonts.googleapis.com/css2?family=Questrial&display=swap">
<style>
  :root {
    --page: #e9e7e3;
    --card-white: #ffffff;
    --brand-blue: #0596c6;
    --brand-blue-light: #8fcbe3;
    --brand-green: #b9d40b;
    --brand-green-deep: #a4c000;
    --brand-green-light: #d3e63a;
    --ink: #3a3a3a;
  }
  * { box-sizing: border-box; margin: 0; padding: 0; }
  html, body {
    width: 1200px; height: 1023px; overflow: hidden;
    background: var(--page);
    font-family: "Questrial", "Century Gothic", sans-serif;
  }
  .sheet {
    position: relative; width: 1200px; height: 1023px;
  }
  .card {
    position: absolute; left: 250px; width: 700px; height: 400px;
    border-radius: 22px; overflow: hidden;
    box-shadow: 0 6px 18px rgba(0,0,0,.18);
  }
  .card--front { top: 85px; background: var(--card-white); }
  .card--back {
    top: 538px;
    background: radial-gradient(ellipse at 40% 40%, var(--brand-green-light), var(--brand-green) 60%, var(--brand-green-deep));
  }
  .brand-art {
    position: absolute; right: 0; top: 0; width: 440px; height: 260px;
    background: linear-gradient(160deg, var(--brand-green) 0%, var(--brand-green) 28%, var(--brand-blue) 29%, var(--brand-blue) 100%);
    border-bottom-left-radius: 120px;
  }
  .person {
    position: absolute; left: 46px; top: 120px;
    color: var(--brand-blue-light);
  }
  .person__name { font-size: 30px; line-height: 1.1; }
  .person__title { font-size: 17px; margin-top: 2px; }
  .front-footer {
    position: absolute; left: 40px; bottom: 34px; right: 30px;
    display: flex; align-items: center; gap: 18px;
  }
  .wordmark {
    display: flex; align-items: center; gap: 8px;
    font-size: 22px; color: var(--brand-blue); white-space: nowrap;
  }
  .wordmark__mark { width: 14px; height: 14px; background: var(--brand-blue); }
  .contact { font-size: 15.5px; color: var(--ink); line-height: 1.45; }
  .contact__label { color: var(--brand-green-deep); font-weight: 400; margin-right: 4px; }
  .contact__item { margin-right: 14px; }
  .back-wordmark {
    position: absolute; left: 0; right: 0; top: 50%; transform: translateY(-50%);
    display: flex; justify-content: center; align-items: center; gap: 12px;
    font-size: 40px; color: var(--card-white);
  }
  .back-wordmark__mark { width: 22px; height: 22px; background: var(--card-white); }
</style>
</head>
<body>
<main class="sheet">
  <section class="card card--front" aria-label="Card front">
    <div class="brand-art" role="img" aria-label="Brand decoration area in blue and green"></div>
    <div class="person">
      <p class="person__name">Dana Whitfield</p>
      <p class="person__title">Director</p>
    </div>
    <div class="front-footer">
      <div class="wordmark"><span class="wordmark__mark"></span>Tallow Crest</div>
      <div class="contact">
        <p>
          <span class="contact__item"><span class="contact__label">P.</span>1877-555-0142</span>
          <span class="contact__item"><span class="contact__label">E.</span>info@tallowcrest.com</span>
          <span><span class="contact__label">W.</span>www.tallowcrest.com</span>
        </p>
        <p>1820 Larkfield Way, Sugar Vale, TX 77401</p>
      </div>
    </div>
  </section>
  <section class="card card--back" aria-label="Card back">
    <div class="back-wordmark"><span class="back-wordmark__mark"></span>Tallow Crest</div>
  </section>
</main>
</body>
</html>
```